Design business card for new business which advocates for elders in nursing homes or personal care h

New business for rights of the elderly residents who reside in personal care homes and or nursing homes. I am looking for a business card with logo of keystone for Pennsylvania and something in side the keystone that represents healthcare, advocates, something on that line; monitor care received and needs of resident. Chart audits, State Regulation compliance

Target Market(s)

Seniors no longer safe to live at home by themselves along with their kids

Industry/Entity Type

Business

Contact Information for Business Card

Keystone symbol to represent Pensylvaoa with some kind of symbol inside to represent advocate, seniors, or healthcare symbol

Font styles to use
Serif

Colors
33a6d7
85cae6
abd037

Requirements
Must have
• Brightwell Elder Allies is our business name; our tag line is Path to Better Living
Nice to have
• Nice logo

```html
<!DOCTYPE html>
<html lang="en">
<head>
<meta charset="utf-8">
<title>Brightwell Elder Allies – Business Card</title>
<link href="https://fonts.googleapis.com/css2?family=Cinzel:wght@400&family=Crimson+Text:wght@400&display=swap" rel="stylesheet">
<style>
  :root {
    --backdrop: #b2b5b6;
    --brand-blue: #2ea5d8;
    --text-blue: #33a6d7;
    --light-blue: #85cae6;
    --lime: #abd037;
    --card-white: #ffffff;
    --shadow: rgba(40, 40, 40, 0.55);
  }
  html, body {
    margin: 0;
    padding: 0;
    overflow: hidden;
  }
  .canvas {
    position: relative;
    width: 1200px;
    height: 1000px;
    background: var(--backdrop);
    overflow: hidden;
  }
  .card {
    position: absolute;
    width: 650px;
    height: 369px;
    box-shadow: 6px 8px 8px var(--shadow);
  }
  .card--front {
    left: 267px;
    top: 68px;
    background: var(--brand-blue);
  }
  .card--back {
    left: 275px;
    top: 528px;
    background: var(--card-white);
  }
  .front-name {
    position: absolute;
    left: 0;
    right: 0;
    top: 128px;
    font-family: "Cinzel", serif;
    font-weight: 400;
    font-size: 40px;
    color: var(--lime);
    text-align: center;
    line-height: 1.2;
    margin: 0;
  }
  .lockup {
    position: absolute;
    left: 114px;
    top: 102px;
    display: flex;
    align-items: center;
  }
  .lockup__mark {
    width: 105px;
    height: 105px;
    background: var(--lime);
  }
  .lockup__divider {
    width: 2px;
    height: 116px;
    background: var(--light-blue);
    margin: 0 22px 0 42px;
  }
  .lockup__text {
    display: flex;
    flex-direction: column;
  }
  .lockup__name {
    font-family: "Cinzel", serif;
    font-weight: 400;
    font-size: 30px;
    line-height: 1.1;
    color: var(--light-blue);
    margin: 0;
  }
  .lockup__tagline {
    font-family: "Crimson Text", serif;
    font-weight: 400;
    font-size: 16px;
    letter-spacing: 0.06em;
    text-transform: uppercase;
    color: var(--text-blue);
    margin: 6px 0 0 2px;
  }
  .contact {
    position: absolute;
    left: 245px;
    top: 262px;
    margin: 0;
    padding: 0;
    list-style: none;
  }
  .contact__item {
    display: flex;
    align-items: center;
    font-family: "Crimson Text", serif;
    font-size: 23px;
    color: var(--text-blue);
    height: 32px;
  }
  .contact__bullet {
    width: 17px;
    height: 17px;
    margin-right: 11px;
  }
  .contact__bullet--blue { background: var(--light-blue); }
  .contact__bullet--lime { background: var(--lime); }
</style>
</head>
<body>
  <div class="canvas">
    <section class="card card--front" aria-label="Card front">
      <p class="front-name">Brightwell<br>Elder Allies</p>
    </section>

    <section class="card card--back" aria-label="Card back">
      <div class="lockup">
        <div class="lockup__mark"></div>
        <div class="lockup__divider"></div>
        <div class="lockup__text">
          <p class="lockup__name">Brightwell<br>Elder Allies</p>
          <p class="lockup__tagline">Path to Better Living</p>
        </div>
      </div>
      <ul class="contact">
        <li class="contact__item"><span class="contact__bullet contact__bullet--blue"></span>555-201-4837</li>
        <li class="contact__item"><span class="contact__bullet contact__bullet--lime"></span>555-374-9120</li>
      </ul>
    </section>
  </div>
</body>
</html>
```